Income Tax Flyer - Updates Needed

Just need to update this flyer design and give it a new look. We would like to keep all the same wording but make it stand out a little more. Our selling point is the "Same Day Tax Advance up to $6,000"

Industry/Entity Type

Lending, Small Loans, Tax Services, Title Loans, Personal Loans

```html
<!DOCTYPE html>
<html lang="en">
<head>
<meta charset="utf-8">
<title>Same Day Tax Advance Flyer</title>
<link rel="stylesheet" href="https://fonts.googleapis.com/css2?family=Montserrat:wght@500;600;700;800;900&display=swap">
<style>
  :root {
    --page: #ffffff;
    --navy-deep: #060d38;
    --navy: #0a1858;
    --navy-card: #13256f;
    --navy-line: #2a3f96;
    --gold: #f8bb0c;
    --gold-light: #ffd54a;
    --orange-top: #ffb515;
    --orange-bottom: #ff7300;
    --white: #ffffff;
    --brand: #0a1858;
    --photo-light: #d9c7b0;
    --photo-dark: #5b4636;
  }
  * { margin: 0; padding: 0; box-sizing: border-box; }
  html, body {
    width: 1200px; height: 1111px; overflow: hidden;
    background: var(--page);
    font-family: "Montserrat", sans-serif;
  }
  .flyer {
    position: absolute; left: 260px; top: 74px;
    width: 680px; height: 962px; overflow: hidden;
    background: linear-gradient(180deg, var(--navy) 0%, var(--navy-deep) 100%);
    color: var(--white);
  }
  .photo {
    position: absolute; left: 0; top: 0; width: 680px; height: 360px;
    background: linear-gradient(120deg, var(--photo-dark) 0%, var(--photo-light) 45%, #8a6f58 100%);
    clip-path: polygon(0 0, 100% 0, 100% 78%, 0 100%);
  }
  .brand-tab {
    position: absolute; left: 0; top: 0; height: 64px; padding: 0 26px 0 22px;
    background: var(--white); border-bottom-right-radius: 22px;
    display: flex; align-items: center; gap: 10px;
  }
  .brand-mark { width: 16px; height: 16px; border-radius: 50%; background: var(--brand); }
  .brand-name { color: var(--brand); font-weight: 700; font-size: 17px; }

  .feature {
    position: absolute; left: 40px; top: 282px; width: 600px; height: 136px;
    border-radius: 20px;
    background: linear-gradient(135deg, var(--gold-light) 0%, var(--gold) 100%);
    box-shadow: 0 14px 30px rgba(0,0,0,0.35);
    display: flex; flex-direction: column; align-items: center; justify-content: center;
    color: var(--navy-deep); text-align: center;
  }
  .feature-lead { font-size: 28px; font-weight: 800; letter-spacing: 1.5px; line-height: 1.1; }
  .feature-amount { font-size: 60px; font-weight: 900; line-height: 1.05; letter-spacing: -0.5px; }

  .headline { position: absolute; left: 40px; top: 452px; width: 600px; }
  .headline-lead { font-size: 30px; font-weight: 600; line-height: 1.1; letter-spacing: 0.5px; }
  .headline-amount { font-size: 56px; font-weight: 800; line-height: 1.1; color: var(--gold); letter-spacing: -0.5px; }
  .headline-day { font-size: 66px; font-weight: 900; line-height: 1.05; letter-spacing: 1px; }

  .offer { position: absolute; left: 40px; top: 640px; width: 600px; border-left: 4px solid var(--gold); padding-left: 14px; }
  .offer-lead { font-size: 17px; font-weight: 600; line-height: 1.3; }
  .offer-highlight { font-size: 24px; font-weight: 800; color: var(--gold); line-height: 1.2; }

  .benefits {
    position: absolute; left: 40px; top: 716px; width: 600px;
    display: flex; justify-content: space-between;
  }
  .benefit {
    width: 190px; height: 108px; border-radius: 14px;
    background: var(--navy-card); border: 1px solid var(--navy-line);
    display: flex; flex-direction: column; align-items: center; justify-content: center;
    text-align: center;
  }
  .benefit svg { width: 36px; height: 36px; display: block; margin-bottom: 8px; }
  .benefit-label { font-size: 13px; font-weight: 600; line-height: 1.25; }

  .contact {
    position: absolute; left: 0; top: 848px; width: 680px; height: 114px;
    background: linear-gradient(90deg, var(--orange-top) 0%, var(--orange-bottom) 100%);
    display: flex; align-items: center; justify-content: space-between;
    padding: 0 40px;
  }
  .contact-heading { color: var(--navy-deep); }
  .contact-lead { font-size: 17px; font-weight: 700; line-height: 1.1; }
  .contact-title { font-size: 38px; font-weight: 900; line-height: 1.05; }
  .contact-details { text-align: right; color: var(--white); }
  .contact-phone { font-size: 17px; font-weight: 700; line-height: 1.3; }
  .contact-line { font-size: 14px; font-weight: 500; line-height: 1.3; }
</style>
</head>
<body>
<main class="flyer">
  <div class="photo" role="img" aria-label="Photo: two women smiling and talking at a laptop in front of a bookshelf"></div>

  <div class="brand-tab"><span class="brand-mark"></span><span class="brand-name">Northvale Financial Group</span></div>

  <section class="feature">
    <div class="feature-lead">SAME DAY TAX ADVANCE</div>
    <div class="feature-amount">UP TO $6,000</div>
  </section>

  <section class="headline">
    <div class="headline-lead">APPLY HERE FOR</div>
    <div class="headline-amount">$5,000-$6,000</div>
    <div class="headline-day">TODAY</div>
  </section>

  <section class="offer">
    <div class="offer-lead">FILE YOUR TAXES AND APPLY FOR AN</div>
    <div class="offer-highlight">EASY ADVANCE!</div>
  </section>

  <section class="benefits">
    <div class="benefit">
      <svg viewBox="0 0 38 38" fill="none" stroke="#f8bb0c" stroke-width="2" stroke-linecap="round">
        <circle cx="19" cy="21" r="13"/><path d="M15 5h8M19 5v3M30 10l2-2"/>
        <text x="19" y="26" font-size="13" font-family="Montserrat, sans-serif" fill="#f8bb0c" stroke="none" text-anchor="middle">$</text>
      </svg>
      <div class="benefit-label">Available In<br>24 Hourse or Less</div>
    </div>
    <div class="benefit">
      <svg viewBox="0 0 38 38" fill="none" stroke="#f8bb0c" stroke-width="2" stroke-linecap="round" stroke-linejoin="round">
        <circle cx="17" cy="15" r="11"/>
        <text x="17" y="20" font-size="12" font-family="Montserrat, sans-serif" fill="#f8bb0c" stroke="none" text-anchor="middle">$</text>
        <path d="M22 20v-2a2 2 0 0 1 4 0v6l4 1a3 3 0 0 1 2 3l-1 6H21l-4-6a2 2 0 0 1 3-3l2 2"/>
      </svg>
      <div class="benefit-label">Choose Your<br>Loan Amount</div>
    </div>
    <div class="benefit">
      <svg viewBox="0 0 38 38" fill="none" stroke="#f8bb0c" stroke-width="2" stroke-linecap="round" stroke-linejoin="round">
        <rect x="11" y="3" width="18" height="28" rx="3" transform="rotate(12 20 17)"/>
        <path d="M15 17l3 3 6-7"/><path d="M6 24l5 8h9l3-5"/>
      </svg>
      <div class="benefit-label">Quick and<br>Easy</div>
    </div>
  </section>

  <section class="contact">
    <div class="contact-heading">
      <div class="contact-lead">CONTACT US</div>
      <div class="contact-title">TODAY!</div>
    </div>
    <div class="contact-details">
      <div class="contact-phone">Phone Number</div>
      <div class="contact-line">Address Line 1</div>
      <div class="contact-line">Address Line 1</div>
      <div class="contact-line">Address Line 1</div>
    </div>
  </section>
</main>
</body>
</html>
```